Label Redesign For Hemp Oil Tincture Bottle*

I need a label redesigned for Marbleleaf Hemp, current bottle label and logo is attached. The current label doesn't standout, not sure if its the font size or colors on the existing label. It is very important to have on the label that this is a Premium Full Spectrum Hemp Oil that is 2000mg. Then after the label is redesigned and approved, I would need to packaging to be designed to match the approved label design.
This Hemp oil has a relaxing effect to help ease mental and emotional stress, tension and worry. The Omega Fatty Acids it contains also naturally improves your mood and overall brain function, causing you to feel more alert and focused. Hemp Oil helps with insomnia. Take some 2-3 hours before bedtime, you will feel relaxed yet aware of how tired you are that it will lead to a good night's sleep. Hemp Oil helps ease chronic pain and inflammation from conditions such as arthritis, fibromyalgia, lupus, and MS. As a pain relief supplement, it is a safer, natural, non-chemical and non-addictive alternative to prescription painkillers.

Target Market(s)

Adults

Industry/Entity Type

Supplement

Font styles to use
Serif
Sans Serif

Colors

Designer to choose colors to be used in the design.

Requirements
Must have
• All information thats on current label but where it says 750 in the front of the existing label, it needs to say 2000. The 2000 should be prominent on the label.

```html
<!DOCTYPE html>
<html lang="en">
<head>
<meta charset="utf-8">
<title>Marbleleaf Hemp – Bottle Label</title>
<link href="https://fonts.googleapis.com/css2?family=Archivo:wght@400;600;800&family=Playfair+Display:ital,wght@0,500;1,600&family=Tinos:ital@0;1&display=swap" rel="stylesheet">
<style>
  :root {
    --page: #ececea;
    --label: #ffffff;
    --leaf-green: #a9c76d;
    --deep-green: #4b6a28;
    --stripe-grey: #c9c9c9;
    --soft-grey: #ededed;
    --ink: #3a3a3a;
    --facts-bg: #eef7d6;
  }
  * { margin: 0; padding: 0; box-sizing: border-box; }
  html, body { width: 852px; height: 1200px; overflow: hidden; }
  body { background: var(--page); position: relative; font-family: "Tinos", serif; color: var(--ink); }

  .label {
    position: absolute; left: 16px; top: 405px; width: 820px; height: 390px;
    background: var(--label); overflow: hidden;
    box-shadow: 0 2px 8px rgba(0,0,0,.15);
  }
  .label-bg { position: absolute; inset: 0; }

  /* left panel */
  .usage { position: absolute; left: 18px; top: 112px; width: 210px; font-size: 9.5px; line-height: 1.45; }
  .usage h3 { font-weight: 400; font-size: 10px; text-transform: uppercase; margin-bottom: 1px; }
  .warning { position: absolute; left: 18px; top: 208px; width: 210px; font-size: 9.5px; line-height: 1.45; }
  .cautions { position: absolute; left: 12px; top: 278px; list-style: none; font-style: italic; font-size: 8.5px; text-transform: uppercase; line-height: 1.1; }
  .cautions li { margin-bottom: 10px; padding-left: 8px; position: relative; }
  .cautions li::before { content: ""; position: absolute; left: 0; top: 3px; width: 3px; height: 3px; border-radius: 50%; background: var(--ink); }

  /* front panel */
  .mandala { position: absolute; left: 275px; top: 70px; width: 235px; height: 235px; border-radius: 50%;
    background: radial-gradient(circle, rgba(0,0,0,.03), rgba(0,0,0,.015) 60%, transparent 70%); }
  .brand-mark { position: absolute; left: 370px; top: 78px; width: 44px; height: 44px; border-radius: 50%; background: var(--deep-green); }
  .zero-thc { position: absolute; left: 232px; width: 323px; top: 160px; text-align: center; font-family: "Playfair Display", serif; font-weight: 500; font-size: 20px; color: #555; }
  .product-name { position: absolute; left: 232px; width: 323px; top: 188px; text-align: center; font-family: "Playfair Display", serif; font-weight: 500; font-size: 33px; color: var(--deep-green); white-space: nowrap; }
  .descriptor { position: absolute; left: 232px; width: 323px; top: 232px; text-align: center; font-family: "Playfair Display", serif; font-style: italic; font-weight: 600; font-size: 16px; line-height: 1.15; color: #333; }
  .strength { position: absolute; left: 331px; top: 280px; width: 118px; height: 66px; background: var(--deep-green); color: #fff; text-align: center; }
  .strength .mg { font-family: "Playfair Display", serif; font-size: 28px; line-height: 1; margin-top: 6px; display: block; }
  .strength .sub { font-size: 9px; line-height: 1.3; display: block; margin-top: 3px; }
  .flavor { position: absolute; left: 262px; top: 357px; width: 262px; display: flex; align-items: center; gap: 5px; font-family: "Playfair Display", serif; font-style: italic; font-weight: 600; font-size: 13px; color: var(--deep-green); white-space: nowrap; }
  .flavor::before, .flavor::after { content: ""; flex: 1; height: 1px; background: var(--ink); }

  /* back panel */
  .facts { position: absolute; left: 608px; top: 28px; width: 177px; background: var(--facts-bg); border: 2px solid var(--leaf-green); font-family: "Archivo", sans-serif; font-size: 8px; color: #333; }
  .facts h2 { font-weight: 800; font-size: 15px; padding: 2px 6px 3px; border-bottom: 2px solid var(--leaf-green); background: #fff; }
  .facts .row { padding: 3px 6px; border-bottom: 1px solid var(--leaf-green); display: flex; justify-content: space-between; }
  .facts .row:last-child { border-bottom: none; display: block; line-height: 1.2; }
  .facts .serving { display: block; line-height: 1.2; }
  .facts b { font-weight: 600; }
  .lot { position: absolute; left: 796px; top: 160px; transform: rotate(-90deg); transform-origin: left top; font-family: "Archivo", sans-serif; font-size: 8px; white-space: nowrap; }
  .distributor { position: absolute; left: 579px; top: 262px; font-size: 14px; line-height: 1.25; color: #555; }
  .distributor a { display: block; font-size: 9.5px; color: var(--deep-green); text-decoration: none; }
</style>
</head>
<body>
<div class="label">
  <svg class="label-bg" viewBox="0 0 820 390" preserveAspectRatio="none" aria-hidden="true">
    <path d="M555 0 H820 V390 H555 Z" fill="var(--soft-grey)" opacity=".55"/>
    <path d="M0 0 H820 V262 C770 252 720 232 650 188 C560 132 480 50 360 36 C240 22 120 50 0 100 Z" fill="var(--stripe-grey)"/>
    <path d="M0 0 H820 V250 C770 240 720 220 650 176 C560 120 480 38 360 24 C240 10 120 38 0 88 Z" fill="var(--label)"/>
    <path d="M0 0 H820 V240 C770 230 720 210 650 166 C560 110 480 28 360 14 C240 0 120 28 0 78 Z" fill="var(--leaf-green)"/>
    <path d="M0 0 H820 V232 C770 222 720 202 650 158 C560 102 480 20 360 6 C240 -8 120 20 0 70 Z" fill="var(--leaf-green)"/>
    <path d="M555 240 C640 280 720 270 820 266 V272 C720 278 640 288 555 252 Z" fill="var(--stripe-grey)"/>
    <line x1="232" y1="0" x2="232" y2="390" stroke="#e2e2e2" stroke-width="1"/>
    <line x1="555" y1="0" x2="555" y2="390" stroke="#e2e2e2" stroke-width="1"/>
  </svg>

  <section class="panel-usage">
    <div class="usage">
      <h3>Suggested Use:</h3>
      <p>Shake well before each use. Take 30 drops (1 full Dropper) and place in mouth underneath tongue for 90 seconds 1-2 times daily or as recommended by a Physician.</p>
    </div>
    <p class="warning">Warnings: If you are pregnant or breastfeeding, Consult health care Practitioner before</p>
    <ul class="cautions">
      <li>Keep out of reach of children</li>
      <li>Do not use if seal is broken<br>or missing</li>
    </ul>
  </section>

  <section class="panel-front">
    <div class="mandala" role="img" aria-label="Faint decorative mandala pattern behind the product name"></div>
    <div class="brand-mark" aria-hidden="true"></div>
    <p class="zero-thc">Zero THC</p>
    <h1 class="product-name">Marbleleaf Hemp</h1>
    <p class="descriptor">Premium Full Spectrum<br>2000 Hemp Oil</p>
    <div class="strength">
      <span class="mg">2000</span>
      <span class="sub">Dietary Supplement<br>1FLOZ (30ML)</span>
    </div>
    <p class="flavor">Natural Peppermint Flavor</p>
  </section>

  <section class="panel-back">
    <div class="facts">
      <h2>Supplement Facts</h2>
      <div class="row"><span class="serving">Serving Size: ml<br>Servings per Container: 30</span></div>
      <div class="row"><b>Calories 8</b><span>Calories from Fat 8</span></div>
      <div class="row"><b>Total Fat</b><b>1g 2%</b></div>
      <div class="row"><span>Full Spectrum Hemp Extract</span><span>24.99mg</span></div>
      <div class="row">Other Ingredients: Hemp seed oil, Grape seed oil, Peppermint and stevia</div>
    </div>
    <p class="lot">LOT#MRV07301BTI Best By: 1/03/20</p>
    <div class="distributor">
      Distributed for:<br>Fernvale Extracts, INC.
      <a href="#">Support@MarbleleafHemp.com</a>
    </div>
  </section>
</div>
</body>
</html>
```